Stationary and document suite for consultancy business in Australia called Lumeta

I would like to get a suite of documents suitable for my new business called Lumeta. I have included the original brief below, however have already selected a design for the logo. I would like to get:
Letter head - simple letter template with "V" logo embossed in background
Word document - standard format with "V" logo embossed in background
Proposal document - bolder pages with cover and back cover, include empty pages with footer as well as contents
Powerpoint presentation - open to ideas
Email signature - banner style or text, open to ideas
Brief that was given for logo (logo not required)
The name of the business is derived from the latin word for green ("Viridis") combined with "co" which is intended to represent a number of different words: collaborative, cooperative, coaching, collective,  construction, consulting, etc.
My objective for the brand is to represent a dynamic, progressive and collaborative business, where our people have fun and enjoy their work.
The objective of our business is to provide consultancy services to construction businesses, mainly aimed at building high performing teams and strategic growth. We will create learning and development tools that businesses can use to increase staff satisfaction and retention. Our future goal is to invest in decarbonisation and sustainability technology for use in the construction industry.
Our target market is construction business leaders and infrastructure owners, who operate road, rail and utility assets. We also want to present as a dynamic, progressive and fun place to work that will be attractive to new employees.

```html
<!DOCTYPE html>
<html lang="en">
<head>
<meta charset="utf-8">
<title>Lumeta Stationery Suite</title>
<link rel="stylesheet" href="https://fonts.googleapis.com/css2?family=Exo+2:wght@400;500;600;700&display=swap">
<style>
  :root {
    --bg: #d4d4d4;
    --green: #8cc63f;
    --green-dark: #6fa92c;
    --charcoal: #444446;
    --grey: #5b5d60;
    --paper: #f6f7f0;
    --white: #ffffff;
    --text: #4a4a4a;
  }
  * { box-sizing: border-box; margin: 0; padding: 0; }
  html, body { width: 1200px; height: 800px; overflow: hidden; }
  body {
    background: var(--bg);
    font-family: "Exo 2", sans-serif;
    color: var(--text);
    position: relative;
  }
  .sheet { position: absolute; box-shadow: 0 4px 10px rgba(0,0,0,.18); }
  .wordmark { font-family: "Exo 2", sans-serif; font-weight: 600; letter-spacing: .02em; line-height: 1; }
  .rule-double {
    position: absolute; height: 4px;
    border-top: 1px solid var(--grey); border-bottom: 1px solid var(--green);
  }
  .signature-space { display: block; height: 6px; border-bottom: 1px solid #c9cbc2; }
  .contact { list-style: none; }
  .contact li { display: flex; align-items: center; gap: 3px; line-height: 1.6; }
  .icon { width: 6px; height: 6px; flex: none; }

  /* Envelope */
  .envelope { left: 190px; top: 274px; width: 265px; height: 353px; background: var(--white); }
  .envelope .sender { position: absolute; left: 20px; top: 316px; width: 48px; font-size: 4px; }
  .envelope .sender .name { color: var(--green); font-weight: 500; margin-top: 3px; }
  .envelope .sender .role { letter-spacing: .08em; }
  .envelope .divider { position: absolute; left: 70px; top: 316px; width: 1px; height: 20px; background: #cfd1c8; }
  .envelope .contact { position: absolute; left: 76px; top: 315px; font-size: 3.2px; }
  .envelope .flap-block { position: absolute; left: 135px; top: 316px; width: 61px; height: 37px; background: var(--green); }
  .envelope .wordmark { position: absolute; left: 207px; top: 323px; font-size: 14px; color: var(--grey); }
  .envelope .base-line { position: absolute; left: 0; bottom: 0; width: 100%; height: 1px; background: var(--green); }

  /* Folder cover */
  .cover { left: 253px; top: 183px; width: 270px; height: 360px; background: var(--green); overflow: hidden; }
  .cover .wordmark { position: absolute; left: 14px; top: 31px; font-size: 19px; color: var(--white); }
  .cover .rule-double { left: 80px; right: 0; top: 39px; border-color: var(--white); }
  .cover .web { position: absolute; left: 165px; top: 331px; display: flex; align-items: center; gap: 5px; color: var(--white); font-size: 7px; letter-spacing: .15em; }
  .cover .web .icon { width: 10px; height: 10px; }

  /* Letterhead */
  .letter { left: 553px; top: 125px; width: 356px; height: 503px; background: var(--paper); overflow: hidden; }
  .letter .head .wordmark { position: absolute; left: 14px; top: 31px; font-size: 23px; color: var(--grey); }
  .letter .head .rule-double { left: 98px; right: 24px; top: 46px; }
  .letter .body { position: absolute; left: 30px; top: 91px; width: 302px; font-size: 6.1px; line-height: 10.7px; text-align: justify; }
  .letter .recipient { font-weight: 500; margin-bottom: 10.7px; }
  .letter .body p { margin-bottom: 10.7px; }
  .letter .closing { margin-top: 10.7px; }
  .letter .closing .name { font-weight: 600; margin-top: 21px; }
  .letter .corner { position: absolute; right: 0; bottom: 0; width: 80px; height: 110px; }
  .letter .foot { position: absolute; left: 0; top: 530px; }
  .letter .foot-wordmark { position: absolute; left: 36px; top: 438px; font-size: 16px; color: var(--grey); }
  .letter .foot-divider { position: absolute; left: 109px; top: 420px; width: 1px; height: 48px; background: #cfd1c8; }
  .letter .foot-details { position: absolute; left: 120px; top: 418px; width: 70px; font-size: 6px; }
  .letter .foot-details .name { color: var(--green); font-weight: 600; margin-top: 6px; }
  .letter .foot-details .role { letter-spacing: .14em; font-weight: 500; color: var(--charcoal); }
  .letter .foot-details .contact { font-size: 4px; margin-top: 3px; }

  /* Landscape business cards */
  .card-h { left: 445px; width: 157px; height: 87px; background: var(--paper); }
  .card-portrait { top: 386px; }
  .card-logo { top: 495px; }
  .card-h .divider { position: absolute; top: 25px; width: 1px; height: 40px; background: #cfd1c8; }
  .card-h .details { position: absolute; font-size: 4.3px; }
  .card-h .details .wordmark { font-size: 14px; color: var(--grey); margin: 4px 0 4px; }
  .card-h .details .name { color: var(--green); font-weight: 600; font-size: 5.6px; margin-top: 5px; }
  .card-h .details .role { letter-spacing: .14em; font-weight: 500; font-size: 5px; color: var(--charcoal); }
  .card-h .contact { font-size: 3.4px; margin-top: 3px; letter-spacing: .06em; }
  .card-portrait .photo {
    position: absolute; left: 29px; top: 21px; width: 30px; height: 30px; border-radius: 50%;
    border: 1.5px solid var(--green);
    background: radial-gradient(circle at 50% 40%, #b89a86 0 35%, #5f86a8 36% 100%);
  }
  .card-portrait .owner { position: absolute; left: 12px; top: 56px; width: 64px; text-align: center; font-size: 4.6px; }
  .card-portrait .owner .name { font-weight: 600; color: var(--charcoal); }
  .card-portrait .owner .role { color: var(--green); letter-spacing: .14em; }
  .card-logo .wordmark-left { position: absolute; left: 8px; top: 36px; font-size: 17px; color: var(--grey); }

  /* Portrait business cards */
  .card-v { left: 932px; width: 103px; height: 180px; }
  .card-light { top: 142px; background: var(--white); }
  .card-light .wordmark { position: absolute; left: 0; width: 100%; top: 46px; text-align: center; font-size: 16px; color: var(--grey); }
  .card-light .name { position: absolute; left: 16px; top: 103px; font-size: 6.4px; font-weight: 700; color: var(--charcoal); }
  .card-light .role { position: absolute; left: 16px; top: 111px; font-size: 5px; font-weight: 500; }
  .card-light .contact { position: absolute; left: 16px; top: 127px; font-size: 4.6px; font-weight: 500; color: var(--charcoal); }
  .card-light .contact .icon { width: 7px; height: 7px; }
  .card-dark { top: 358px; background: var(--charcoal); }
  .card-dark .wordmark { position: absolute; left: 0; width: 100%; top: 24px; text-align: center; font-size: 17px; color: var(--white); }
  .card-dark .web { position: absolute; left: 40px; top: 157px; display: flex; align-items: center; gap: 2px; color: var(--white); font-size: 4.6px; font-weight: 600; letter-spacing: .12em; }
  .card-dark .web .icon { width: 4px; height: 4px; }
</style>
</head>
<body>

<svg width="0" height="0" style="position:absolute" aria-hidden="true">
  <defs>
    <symbol id="icon-phone" viewBox="0 0 10 10">
      <circle cx="5" cy="5" r="5" fill="#8cc63f"/>
      <path d="M3.2 2.6 L4.2 2.4 L4.7 3.8 L4.1 4.3 Q4.7 5.5 5.7 5.9 L6.2 5.3 L7.6 5.8 L7.4 6.8 Q4 7 3.2 2.6 Z" fill="#fff"/>
    </symbol>
    <symbol id="icon-mail" viewBox="0 0 10 10">
      <circle cx="5" cy="5" r="5" fill="#8cc63f"/>
      <rect x="2.6" y="3.3" width="4.8" height="3.4" fill="none" stroke="#fff" stroke-width=".7"/>
      <path d="M2.6 3.3 L5 5.2 L7.4 3.3" fill="none" stroke="#fff" stroke-width=".7"/>
    </symbol>
    <symbol id="icon-web" viewBox="0 0 10 10">
      <circle cx="5" cy="5" r="5" fill="#8cc63f"/>
      <circle cx="5" cy="5" r="2.6" fill="none" stroke="#fff" stroke-width=".6"/>
      <path d="M2.4 5 H7.6 M5 2.4 Q3.6 5 5 7.6 M5 2.4 Q6.4 5 5 7.6" fill="none" stroke="#fff" stroke-width=".5"/>
    </symbol>
  </defs>
</svg>

<section class="sheet envelope" aria-label="Envelope">
  <div class="sender">
    <span class="signature-space" role="img" aria-label="Handwritten signature"></span>
    <div class="name">NORA ELLISON</div>
    <div class="role">Director</div>
  </div>
  <div class="divider"></div>
  <ul class="contact">
    <li><svg class="icon"><use href="#icon-phone"/></svg>+61 400 518 302</li>
    <li><svg class="icon"><use href="#icon-mail"/></svg>nora@lumeta.com.au</li>
    <li><svg class="icon"><use href="#icon-web"/></svg>lumeta.com.au</li>
  </ul>
  <div class="flap-block"></div>
  <div class="wordmark">Lumeta</div>
  <div class="base-line"></div>
</section>

<section class="sheet cover" aria-label="Presentation folder cover">
  <div class="wordmark">Lumeta</div>
  <div class="rule-double"></div>
  <div class="web"><svg class="icon"><use href="#icon-web"/></svg>lumeta.com.au</div>
</section>

<section class="sheet letter" aria-label="Letterhead">
  <header class="head">
    <div class="wordmark">Lumeta</div>
    <div class="rule-double"></div>
  </header>
  <div class="body">
    <div class="recipient">To,<br>Mr. Peter Hale<br>Chairman<br>Australia</div>
    <p>Dear Sir,<br>This is a sample letter that has been placed to demonstrate the typing format on the (Your Company) letterhead design. When positioned properly, it will serve to work in harmony with all of the other elements on the letterhead.</p>
    <p>This letterhead design is meant to project an image of professionalism and reliability. By using simple alignments we have created a very spacious feeling. The simplicity suggests strength and the spaciousness contributes to the aesthetics of the layout. These basic qualities along with the (Your Company) colours, are consistent with the overall look and helps to reinforce the (Your Company) brand. This letterhead design is meant to project an image of professionalism and reliability.</p>
    <p>The simplicity suggests strength and the spaciousness contributes to the aesthetics of the layout. These basic qualities along with the (Your Company) colours, are consistent with the overall look and helps to reinforce the (Your Company) brand. This letterhead design is meant to project an image of professionalism and reliability.<br>This letterhead design is based on the (Form of your logo) form the (Your Company) logo. Each stationery item is part of the (Form of your logo).</p>
    <div class="closing">
      Sincerely yours,
      <div class="name">Nora Ellison</div>
      <div>Director</div>
    </div>
  </div>
  <svg class="corner" viewBox="0 0 80 110" aria-hidden="true">
    <path d="M0 8 Q55 0 80 30 L80 110 Q70 40 0 8 Z" fill="var(--green)"/>
  </svg>
  <div class="foot-wordmark wordmark">Lumeta</div>
  <div class="foot-divider"></div>
  <div class="foot-details">
    <span class="signature-space" role="img" aria-label="Handwritten signature"></span>
    <div class="name">NORA ELLISON</div>
    <div class="role">Director</div>
    <ul class="contact">
      <li><svg class="icon"><use href="#icon-phone"/></svg>+61 400 518 302</li>
      <li><svg class="icon"><use href="#icon-mail"/></svg>nora@lumeta.com.au</li>
      <li><svg class="icon"><use href="#icon-web"/></svg>lumeta.com.au</li>
    </ul>
  </div>
</section>

<section class="sheet card-h card-portrait" aria-label="Business card with portrait">
  <div class="photo" role="img" aria-label="Portrait photo of the director"></div>
  <div class="owner">
    <div class="name">NORA ELLISON</div>
    <div class="role">Director</div>
  </div>
  <div class="divider" style="left:74px"></div>
  <div class="details" style="left:89px; top:25px">
    <span class="signature-space" role="img" aria-label="Handwritten signature" style="width:48px"></span>
    <div class="wordmark">Lumeta</div>
    <ul class="contact">
      <li><svg class="icon"><use href="#icon-phone"/></svg>+61 400 518 302</li>
      <li><svg class="icon"><use href="#icon-web"/></svg>lumeta.com.au</li>
    </ul>
  </div>
</section>

<section class="sheet card-h card-logo" aria-label="Business card">
  <div class="wordmark wordmark-left">Lumeta</div>
  <div class="divider" style="left:79px"></div>
  <div class="details" style="left:91px; top:26px">
    <span class="signature-space" role="img" aria-label="Handwritten signature" style="width:48px"></span>
    <div class="name">NORA ELLISON</div>
    <div class="role">Director</div>
    <ul class="contact">
      <li><svg class="icon"><use href="#icon-phone"/></svg>+61 400 518 302</li>
      <li><svg class="icon"><use href="#icon-web"/></svg>lumeta.com.au</li>
    </ul>
  </div>
</section>

<section class="sheet card-v card-light" aria-label="Business card front">
  <div class="wordmark">Lumeta</div>
  <div class="name">NORA ELLISON</div>
  <div class="role">Director</div>
  <ul class="contact">
    <li><svg class="icon"><use href="#icon-phone"/></svg>+61 400 518 302</li>
    <li><svg class="icon"><use href="#icon-mail"/></svg>nora@lumeta.com.au</li>
    <li><svg class="icon"><use href="#icon-web"/></svg>lumeta.com.au</li>
  </ul>
</section>

<section class="sheet card-v card-dark" aria-label="Business card back">
  <div class="wordmark">Lumeta</div>
  <div class="web"><svg class="icon"><use href="#icon-web"/></svg>lumeta.com.au</div>
</section>

</body>
</html>
```